Swiss Consultant for Enterprises and SME's is in Need for PPT for Teaching/Presenting

I am looking for a powerpointpresentation template (must be with slidemaster) for presenting my company and also for teaching. Colors must be taken from Logo and content can be taken from website if needed.

It is either used to present anything regarding finances and ERP-Systemrelated topics (espeically VEX Trade Suite) and also teach anything regarding Finance and or ERP-Systems in an industrial or financial environment.
Updates

Low design quality

Font styles to use
Sans Serif

Requirements
Must have
• I need at least following slides (Title, Subtitle/Section, Index, Single content, Empty (just logo), two content, tree content -> each as column and at last 4 / 5 & 6 infographics (done with o365 "standard" Icons)
• Coloring white and same as logo provided no additional colors except for charts etc.(matching to logostyle)
• Also I need a Word template such as the one attached.
Nice to have
• any additional infographic
Should not have
• Presentation must be done in the slidemaster as a template anything else will not be accepted.
• Letterhead is not needed I only need a Document for Documentation.

```html
<!DOCTYPE html>
<html lang="en">
<head>
<meta charset="utf-8">
<title>Project Title Here</title>
<link href="https://fonts.googleapis.com/css2?family=Exo+2:wght@700&family=Montserrat:wght@400;500;600;700&display=swap" rel="stylesheet">
<style>
  :root {
    --bg: #ededed;
    --brand-blue: #2f73b7;
    --sky: #00aeef;
    --mid-blue: #1f74bd;
    --teal: #36acd5;
    --slate: #5b5b5b;
    --sage: #a9c0c0;
    --sand: #c4b59a;
    --grid: #cfcfcf;
    --axis-text: #9a9a9a;
    --body-text: #7a7a7a;
    --accent-yellow: #e3d91a;
    --white: #ffffff;
  }
  * { margin: 0; padding: 0; box-sizing: border-box; }
  html, body { width: 1200px; height: 900px; overflow: hidden; }
  body { background: #ffffff; }
  .slide {
    position: relative;
    width: 1200px;
    height: 900px;
    overflow: hidden;
    background: var(--bg);
    font-family: "Montserrat", Arial, sans-serif;
  }
  .slide-title {
    position: absolute;
    left: 27px;
    top: 33px;
    font-family: "Exo 2", "Montserrat", sans-serif;
    font-weight: 700;
    font-size: 34px;
    letter-spacing: 0.5px;
    color: var(--brand-blue);
  }
  .title-rule {
    position: absolute;
    left: 0;
    top: 76px;
    width: 367px;
    height: 4px;
    background: var(--brand-blue);
  }
  .brand {
    position: absolute;
    right: 20px;
    top: 28px;
    display: flex;
    align-items: center;
    gap: 12px;
  }
  .brand-mark {
    width: 18px;
    height: 18px;
    background: var(--brand-blue);
  }
  .brand-name {
    font-weight: 700;
    font-size: 30px;
    color: var(--brand-blue);
    line-height: 1;
  }
  .chart {
    position: absolute;
    left: 0;
    top: 0;
  }
  .chart .gridline { stroke: var(--grid); stroke-width: 1.5; }
  .chart .axis-value, .chart .axis-month {
    font-family: "Montserrat", Arial, sans-serif;
    font-weight: 600;
    fill: var(--axis-text);
  }
  .chart .axis-value { font-size: 18px; }
  .chart .axis-month { font-size: 18px; }
  .subtext {
    position: absolute;
    left: 75px;
    top: 663px;
    width: 1050px;
  }
  .subtext-heading {
    font-weight: 500;
    font-size: 27px;
    color: var(--sky);
    margin-bottom: 4px;
  }
  .subtext-body {
    font-size: 18.5px;
    line-height: 34.5px;
    color: var(--body-text);
    text-align: justify;
  }
  .footer-band {
    position: absolute;
    left: 0;
    bottom: 0;
    width: 1200px;
    height: 27px;
    background: var(--accent-yellow);
  }
  .page-marker {
    position: absolute;
    right: 0;
    bottom: 0;
  }
  .page-number {
    font-family: "Montserrat", Arial, sans-serif;
    font-size: 26px;
    font-weight: 500;
    fill: var(--white);
  }
</style>
</head>
<body>
<main class="slide">
  <h1 class="slide-title">PROJECT TITLE HERE</h1>
  <div class="title-rule"></div>

  <div class="brand">
    <span class="brand-mark"></span>
    <span class="brand-name">Kernwald Consulting</span>
  </div>

  <svg class="chart" width="1200" height="640" viewBox="0 0 1200 640" role="img" aria-label="Monthly bar chart from January to December">
    <g class="grid">
      <line class="gridline" x1="93" y1="201" x2="1148" y2="201"/>
      <line class="gridline" x1="93" y1="295.5" x2="1148" y2="295.5"/>
      <line class="gridline" x1="93" y1="390" x2="1148" y2="390"/>
      <line class="gridline" x1="93" y1="484.5" x2="1148" y2="484.5"/>
      <line class="gridline" x1="93" y1="579" x2="1148" y2="579"/>
    </g>
    <g class="axis-values">
      <text class="axis-value" x="60" y="198">100</text>
      <text class="axis-value" x="68" y="292">75</text>
      <text class="axis-value" x="68" y="387">50</text>
      <text class="axis-value" x="68" y="481">25</text>
      <text class="axis-value" x="78" y="576">0</text>
    </g>
    <g class="bars">
      <rect x="129" y="427.8" width="48" height="151.2" fill="var(--slate)"/>
      <rect x="213" y="314.4" width="48" height="264.6" fill="var(--sky)"/>
      <rect x="298.5" y="352.2" width="48" height="226.8" fill="var(--mid-blue)"/>
      <rect x="382.5" y="287.9" width="48" height="291.1" fill="var(--teal)"/>
      <rect x="468" y="363.5" width="48" height="215.5" fill="var(--sky)"/>
      <rect x="553.5" y="314.4" width="48" height="264.6" fill="var(--sage)"/>
      <rect x="637.5" y="333.3" width="48" height="245.7" fill="var(--mid-blue)"/>
      <rect x="723" y="219.9" width="48" height="359.1" fill="var(--teal)"/>
      <rect x="808.5" y="295.5" width="48" height="283.5" fill="var(--sand)"/>
      <rect x="892.5" y="250.1" width="48" height="328.9" fill="var(--sage)"/>
      <rect x="978" y="325.7" width="48" height="253.3" fill="var(--mid-blue)"/>
      <rect x="1063.5" y="276.6" width="48" height="302.4" fill="var(--teal)"/>
    </g>
    <g class="axis-months" text-anchor="middle">
      <text class="axis-month" x="153" y="622">JAN</text>
      <text class="axis-month" x="237" y="622">FEB</text>
      <text class="axis-month" x="322.5" y="622">MAR</text>
      <text class="axis-month" x="406.5" y="622">APR</text>
      <text class="axis-month" x="492" y="622">MAY</text>
      <text class="axis-month" x="577.5" y="622">JUN</text>
      <text class="axis-month" x="661.5" y="622">JUL</text>
      <text class="axis-month" x="747" y="622">AUG</text>
      <text class="axis-month" x="832.5" y="622">SEP</text>
      <text class="axis-month" x="916.5" y="622">OCT</text>
      <text class="axis-month" x="1002" y="622">NOV</text>
      <text class="axis-month" x="1087.5" y="622">DEC</text>
    </g>
  </svg>

  <section class="subtext">
    <h2 class="subtext-heading">Subtext here</h2>
    <p class="subtext-body">Lorem Ipsum is simply dummy text of the printing and typesetting industry. Lorem Ipsum has been the industry's standard dummy text ever since the 1500s, when an unknown printer took a galley of type and scrambled it to make a type specimen book. It has survived not only five centuries, but also the leap into electronic typesetting, remaining essentially unchanged.</p>
  </section>

  <div class="footer-band"></div>
  <svg class="page-marker" width="100" height="62" viewBox="0 0 100 62" aria-label="Page 1">
    <polygon points="12,62 50,2 88,62" fill="var(--brand-blue)"/>
    <text class="page-number" x="50" y="54" text-anchor="middle">1</text>
  </svg>
</main>
</body>
</html>
```